Business Card Upgrade

I have designed our business card using our new logo. I think it needs imporovements. We used to have two cards for our business. One card was for our software business, and the other was for our consulting business. We are now in the process of combining our websites, marketing, name, and a new logo.

Our goal is to have a really sharp professional logo. One reason I designed the card the way I did was that our Titles are sometimes long, and by separating the person's name and title, it shows up very well and the title can be adjusted no matter how long it is. Sometimes the title can be 4 or 5 words or more.

We really like our logo on black as it shows up very nice. Our PMS colors are as follows: 368C and 459C.

The Designer that will be working with us will need to deliver the following:

The front and back of the Business Card Design will need to be delivered in a high quality JPEG, and
The front and back of the Business Card Design in Illustrator Format .ai
Any fonts will need to be sent to us if they are not standard and are required to open the Illustrator file correctly.

To help us get a good idea of the card with a title, please use the title: " Director of Software Development "

NOTE: The chosen designer will be selected to design our new letterhead within 2 weeks from the closing of this contest.

To help us make sure the card design works with longer titles, please use the followign job title on the card:  

"Director of Software and Product Development"

 

ALL DESIGNERS:

1. I appreciate the different angles you are showing the cards, but please be sure and always show the direct view, so I can see the layout and what the person I hand the card will see.

2. Please do not use white.  Please use off white as I don't care for white cards and they get dirty easy and do not represent the designs well.

Dear Designers,

Please provide samples straight one as a viewer of the card will see.  Some of the angles that are presented make it impossible to tell how everything fits, and sometimes even makes areas look skewed. So, please provide a straight sample view.

Pinnacle 400 company executives such as Vice Presidents, and Directors

Software

• Professional looking Card.

Our customers are Directors, Vice Presidents, and Presidents of companies as large as Pinnacle 400 companies. The card needs to get attention wile still looking professional.

Delivery of the finished product in Illustrator Format with any fonts needed to edit the text or open the file.

The card will be a heavy stock with a soft touch coating for that silk feel.

```html
<!DOCTYPE html>
<html lang="en">
<head>
<meta charset="utf-8">
<title>Meridian Trade Group — Business Card</title>
<link href="https://fonts.googleapis.com/css2?family=Open+Sans:wght@400;600;700&display=swap" rel="stylesheet">
<style>
  :root {
    --backdrop: #2a2a2c;
    --card: #131217;
    --green: #78be20;
    --gold: #ddd48a;
    --text: #c9c9c9;
    --map-light: #3a3a3e;
    --map-dark: #131217;
  }
  * { margin: 0; padding: 0; box-sizing: border-box; }
  html, body {
    width: 1200px; height: 900px; overflow: hidden;
    background: var(--backdrop);
    font-family: "Open Sans", Arial, sans-serif;
  }
  .card {
    position: absolute;
    top: 295px;
    width: 540px; height: 310px;
    background: var(--card);
    box-shadow: 0 6px 18px rgba(0,0,0,.45);
    overflow: hidden;
  }
  .card--front { left: 40px; }
  .card--back { left: 620px; }

  .world-map {
    position: absolute;
    left: 40px; top: 30px; width: 460px; height: 235px;
    background: radial-gradient(ellipse at 50% 35%, var(--map-light) 0%, #222226 45%, var(--map-dark) 80%);
    border-radius: 40% 40% 45% 45%;
  }
  .brand {
    position: absolute;
    color: var(--green);
    font-weight: 700;
    letter-spacing: .04em;
    text-transform: uppercase;
    line-height: 1.1;
  }
  .card--front .brand {
    left: 0; right: 0; top: 118px;
    text-align: center;
    font-size: 32px;
  }
  .website {
    position: absolute;
    left: 0; right: 0; top: 262px;
    text-align: center;
    color: var(--green);
    font-size: 13px;
  }

  .person { position: absolute; left: 36px; top: 38px; }
  .person__name { color: var(--green); font-size: 19px; font-weight: 400; }
  .person__title { color: var(--gold); font-size: 13px; font-weight: 600; line-height: 19px; margin-top: 3px; }

  .contact { position: absolute; left: 36px; font-size: 13px; line-height: 19px; color: var(--text); }
  .contact--direct { top: 118px; }
  .contact--office { top: 189px; }
  .contact__label { color: var(--green); margin-right: 4px; }

  .card--back .brand {
    right: 34px; top: 208px;
    text-align: right;
    font-size: 24px;
  }
</style>
</head>
<body>
  <section class="card card--front">
    <div class="world-map" role="img" aria-label="Faint world map in dark grey tones"></div>
    <div class="brand">Meridian<br>Trade Group</div>
    <div class="website">www.MERIDIANTRADE.com</div>
  </section>

  <section class="card card--back">
    <div class="person">
      <div class="person__name">Daniel Hartwell</div>
      <div class="person__title">Director of Software<br>and Product Development</div>
    </div>
    <div class="contact contact--direct">
      <div><span class="contact__label">Direct</span>(555) 318-2047</div>
      <div><span class="contact__label">Email</span> d.hartwell@meridiantrade.com</div>
    </div>
    <div class="contact contact--office">
      <div>1480 Harbor View Road</div>
      <div>Bayport, Alabama 36690</div>
      <div><span class="contact__label">Tel</span> (555) 318-2000</div>
      <div><span class="contact__label">Fax</span>(555) 318-2001</div>
    </div>
    <div class="brand">Meridian<br>Trade Group</div>
  </section>
</body>
</html>
```